The Velvet Compass: A Patient Method for Mending Old Maps

This will be for both the hard cover and paperback version. A core theme of the book and what we want to cover to convey is the journey or transformation to "happiness". Concepts such as road/pathway, mountain top, sunrise, dark to bright colors, out-of-focus to in-focus, clouds parting, etc., all represent this idea. I am attaching a 1-page book summary for more information. I like the idea of the subtitle being in a gold seal, but that is not necessary. I am open to any designs, but it should at least be conceptually related to the book.

```html
<!DOCTYPE html>
<html lang="en">
<head>
<meta charset="utf-8">
<title>The Velvet Compass – Book Cover</title>
<link rel="stylesheet" href="https://fonts.googleapis.com/css2?family=Fira+Sans+Extra+Condensed:wght@500;600&display=swap">
<style>
  :root {
    --page-bg: #ffffff;
    --ink-dark: #10231f;
    --ink-teal: #0d5e72;
    --ink-light: #ffffff;
    --sky-top: #b9c6d8;
    --sky-mid: #dfe4ec;
    --sky-low: #eef0f3;
    --mountain-snow: #c6cdda;
    --mountain: #5a6b92;
    --mountain-deep: #3f4f75;
    --forest-light: #4f8a33;
    --forest: #1f4a22;
    --forest-deep: #173a1a;
    --meadow: #a6c43e;
    --meadow-gold: #bdb446;
  }
  html, body {
    margin: 0;
    width: 1200px;
    height: 960px;
    overflow: hidden;
    background: var(--page-bg);
  }
  .book-cover {
    position: absolute;
    left: 307px;
    top: 40px;
    width: 586px;
    height: 880px;
    overflow: hidden;
    font-family: "Fira Sans Extra Condensed", "Arial Narrow", sans-serif;
    box-shadow: 0 2px 6px rgba(0,0,0,0.18);
  }
  .cover-photo {
    position: absolute;
    inset: 0;
    background:
      radial-gradient(ellipse 60% 9% at 50% 45%, rgba(214,220,232,0.9), rgba(214,220,232,0) 100%),
      radial-gradient(ellipse 45% 10% at 15% 62%, rgba(40,70,45,0.55), rgba(40,70,45,0) 100%),
      radial-gradient(ellipse 45% 10% at 88% 62%, rgba(40,70,45,0.55), rgba(40,70,45,0) 100%),
      linear-gradient(180deg,
        var(--sky-top) 0%,
        var(--sky-mid) 18%,
        var(--sky-low) 38%,
        var(--mountain-snow) 46%,
        var(--mountain) 53%,
        var(--mountain-deep) 61%,
        var(--forest-light) 66%,
        var(--forest) 73%,
        var(--forest-deep) 82%,
        #2f5d25 86%,
        var(--meadow) 90%,
        var(--meadow-gold) 100%);
  }
  .title-block { margin: 0; }
  .title {
    position: absolute;
    left: 0;
    right: 0;
    text-align: center;
    line-height: 1;
    font-weight: 500;
  }
  .title-article {
    top: 22px;
    font-size: 128px;
    color: var(--ink-dark);
    letter-spacing: -1px;
  }
  .title-main {
    top: 108px;
    font-size: 164px;
    color: var(--ink-teal);
    letter-spacing: -2px;
  }
  .title-second {
    top: 228px;
    font-size: 164px;
    color: var(--ink-dark);
    letter-spacing: -2px;
  }
  .subtitle {
    position: absolute;
    left: 0;
    right: 0;
    top: 622px;
    margin: 0;
    text-align: center;
    color: var(--ink-light);
    font-weight: 500;
    line-height: 1.35;
  }
  .subtitle-lead {
    display: block;
    font-size: 47px;
    letter-spacing: -0.5px;
  }
  .subtitle-key {
    display: block;
    font-size: 54px;
    font-weight: 600;
  }
  .author {
    position: absolute;
    right: 56px;
    top: 796px;
    margin: 0;
    font-size: 42px;
    font-weight: 600;
    color: var(--ink-dark);
    letter-spacing: -0.5px;
  }
</style>
</head>
<body>
  <main class="book-cover">
    <div class="cover-photo" role="img" aria-label="Photograph of a snow-capped mountain under a cloudy sky, above a dark evergreen forest and a sunlit green meadow"></div>
    <h1 class="title-block">
      <span class="title title-article">THE</span>
      <span class="title title-main">Velvet</span>
      <span class="title title-second">Compass</span>
    </h1>
    <p class="subtitle">
      <span class="subtitle-lead">A Patient Method for Mending</span>
      <span class="subtitle-key">OLD MAPS</span>
    </p>
    <p class="author">ELIAS R. THORNBURY</p>
  </main>
</body>
</html>
```